Antibacterial Hand Wash Squeeze Tube Label

We're looking for a contemporary label design for a new Antibacterial Hand Wash for an 8oz squeeze tube. The new consumer brand will be sold to consumers in major US retail stores & online. The moisturizing hand wash contains Aloe Vera, vitamin E, and other natural ingredients so the design should include the color green. Real photos are very effective on packaging, so a picture of Aloe Vera or possibly two hands washing would help draw consumers' attention to the tube on the retail shelf. The front label may wrap around the sides. Rear must be left mostly blank
US Consumers - retail stores & online
Consumer

```html
<!DOCTYPE html>
<html lang="en">
<head>
<meta charset="UTF-8">
<title>Antibacterial &amp; Moisturizing Hand Wash – Tube Label</title>
<link href="https://fonts.googleapis.com/css2?family=Montserrat:wght@400;500;800&display=swap" rel="stylesheet">
<style>
  :root {
    --page-bg: #ffffff;
    --leaf-green: #5cb83f;
    --leaf-pale: #cfe8b8;
    --brand-green: #16913f;
    --ink: #1b1b1b;
    --aloe-deep: #3fae2f;
    --aloe-light: #9edc7e;
    --skin: #e8c7b5;
    --skin-light: #f6e4da;
  }
  * { margin: 0; padding: 0; box-sizing: border-box; }
  html, body {
    width: 1200px;
    height: 752px;
    overflow: hidden;
    background: var(--page-bg);
  }
  .label {
    position: absolute;
    left: 306px;
    top: 46px;
    width: 588px;
    height: 660px;
    background: linear-gradient(180deg, var(--leaf-green) 0%, #8fcd70 12%, var(--leaf-pale) 26%, #ffffff 42%, #ffffff 100%);
    box-shadow: 0 10px 40px rgba(0,0,0,0.12);
    font-family: "Montserrat", sans-serif;
  }
  .vertical {
    position: absolute;
    transform-origin: left top;
    transform: rotate(-90deg);
    white-space: nowrap;
  }
  .product-claim {
    left: 50px;
    top: 470px;
    font-size: 18px;
    font-weight: 500;
    letter-spacing: 0.9px;
    color: var(--ink);
    line-height: 20px;
  }
  .product-name {
    left: 72px;
    top: 468px;
    font-size: 47px;
    font-weight: 800;
    letter-spacing: 0.5px;
    color: var(--brand-green);
    line-height: 50px;
  }
  .ingredients {
    position: absolute;
    left: 132px;
    top: 232px;
    list-style: none;
    color: var(--brand-green);
    font-size: 14.2px;
    font-weight: 500;
    line-height: 18px;
    letter-spacing: 0.3px;
  }
  .ingredients li::before { content: "+ "; }
  .ingredients li.continued { padding-left: 7px; }
  .ingredients li.continued::before { content: ""; }
  .aloe-leaves {
    position: absolute;
    left: 296px;
    top: 226px;
    width: 134px;
    height: 124px;
    border-radius: 60px 60px 10px 10px;
    background: linear-gradient(180deg, rgba(92,184,63,0.35) 0%, var(--aloe-deep) 100%);
  }
  .aloe-segments {
    position: absolute;
    left: 189px;
    top: 338px;
    width: 210px;
    height: 186px;
    border-radius: 30px;
    background: radial-gradient(ellipse at 40% 50%, var(--aloe-light) 0%, var(--aloe-deep) 70%, #54b83c 100%);
  }
  .hands-photo {
    position: absolute;
    left: 57px;
    top: 476px;
    width: 241px;
    height: 110px;
    border-radius: 50px;
    background: radial-gradient(ellipse at 45% 55%, var(--skin) 0%, var(--skin-light) 60%, rgba(255,255,255,0) 100%);
  }
  .net-weight {
    position: absolute;
    left: 249px;
    top: 591px;
    transform: translateX(-50%);
    font-size: 13.5px;
    font-weight: 500;
    color: var(--ink);
  }
</style>
</head>
<body>
  <main class="label">
    <div class="hands-photo" role="img" aria-label="Photo of two hands lathering with soap"></div>
    <div class="aloe-leaves" role="img" aria-label="Photo of upright fresh aloe vera leaves"></div>
    <div class="aloe-segments" role="img" aria-label="Photo of stacked cut aloe vera leaf segments"></div>

    <p class="vertical product-claim">ANTIBACTERIAL &amp; MOISTURIZING</p>
    <h1 class="vertical product-name">HAND WASH</h1>

    <ul class="ingredients">
      <li>ALOE VERA</li>
      <li>VITAMIN E</li>
      <li>OTHER NATURAL</li>
      <li class="continued">INGREDIENTS</li>
    </ul>

    <p class="net-weight">8 oz</p>
  </main>
</body>
</html>
```